Catchy Cards for Hospital

I run a rural hospital in Texas called Pellor Valley Hospital and am in need of contemporary business cards for all of my Department Heads. While our logo is somewhat simplistic, I don't have the option of changing it at this time, so anything to make the rest of the card present the appearance of a modern, professional healthcare facility would be great. Although the attached files are in black, our hospital colors are in a copper brown and black. I need to be able to change the name and title on the card so I can get cards printed for various department heads.

Target Market(s)

Referring physicians, large hospital systems, national organizations, state and federal government

Industry/Entity Type

Hospital

Contact Information for Business Card

Name Dale Hoskin
Title CEO

Phone: Main 325-555-0147 & Direct xxxxxx
Fax xxxxx
dale.hoskin@pellorvh.example
382 Wimble Street Box 415
Alder Flats, Westmark 76902

Font styles to use
Serif

Colors
f48340

Requirements
Must have
• Clean crisp lines and ability to modify names, titles and emails
• On the back "PellorValleyHospital.Example
Nice to have
• Needs to be in line with logo, which is a bit dated and not too appealing, but I'm hoping that the rest of the card can make up for that fact just a little bit.
• Hospital's colors are a copper brown, black and white
Should not have
• Shapes or anything distracting

```html
<!DOCTYPE html>
<html lang="en">
<head>
<meta charset="utf-8">
<title>Pellor Valley Hospital – Business Card</title>
<link rel="stylesheet" href="https://fonts.googleapis.com/css2?family=Noto+Serif:wght@400;700&display=swap">
<style>
  :root {
    --copper: #f48340;
    --card: #262626;
    --mark: #0e0e0e;
    --backdrop: #5d646c;
  }
  * { margin: 0; padding: 0; box-sizing: border-box; }
  html, body {
    width: 1200px;
    height: 1200px;
    overflow: hidden;
    background: var(--backdrop);
  }
  body {
    position: relative;
    font-family: "Noto Serif", serif;
    color: var(--copper);
  }
  .card {
    position: absolute;
    left: 169px;
    width: 860px;
    height: 496px;
    background: var(--card);
    border: 10px solid var(--copper);
  }
  .card--back { top: 31px; }
  .card--front { top: 610px; }

  .web-address {
    position: absolute;
    inset: 0;
    display: flex;
    align-items: center;
    justify-content: center;
    padding-bottom: 10px;
    font-weight: 700;
    font-size: 24px;
    letter-spacing: 0.2px;
  }

  .person {
    position: absolute;
    left: 49px;
    top: 38px;
  }
  .person__name {
    font-weight: 700;
    font-size: 28px;
    line-height: 1.2;
  }
  .person__title {
    font-size: 19px;
    margin-top: 4px;
  }

  .contact {
    position: absolute;
    left: 49px;
    top: 192px;
    font-size: 14px;
    line-height: 24px;
  }
  .contact__row {
    display: flex;
    margin-bottom: 18px;
  }
  .contact__label {
    width: 69px;
    font-weight: 700;
  }
  .contact__value { font-weight: 400; }
  .contact__value span { display: block; line-height: 19px; }
  .contact__row--address .contact__value { padding-top: 2px; }

  .divider {
    position: absolute;
    left: 416px;
    top: 90px;
    width: 8px;
    height: 294px;
  }

  .brand-name {
    position: absolute;
    left: 560px;
    top: 165px;
    font-size: 30px;
    line-height: 1.05;
    font-weight: 400;
    color: var(--mark);
  }
  .brand-name span { display: block; }
</style>
</head>
<body>
  <section class="card card--back">
    <p class="web-address">PellorValleyHospital.Example</p>
  </section>

  <section class="card card--front">
    <div class="person">
      <h1 class="person__name">Dale Hoskin</h1>
      <p class="person__title">CEO</p>
    </div>

    <div class="contact">
      <div class="contact__row">
        <span class="contact__label">Phone</span>
        <span class="contact__value"><span>325-555-0147</span><span>325-555-0147</span></span>
      </div>
      <div class="contact__row">
        <span class="contact__label">Fax</span>
        <span class="contact__value">456-555-0182</span>
      </div>
      <div class="contact__row">
        <span class="contact__label">E-mail</span>
        <span class="contact__value">dale.hoskin@pellorvh.example</span>
      </div>
      <div class="contact__row contact__row--address">
        <span class="contact__label">Address</span>
        <span class="contact__value"><span>382 Wimble Street Box 415</span><span>Alder Flats, Westmark 76902</span></span>
      </div>
    </div>

    <svg class="divider" viewBox="0 0 8 294" aria-hidden="true">
      <polygon points="1,0 7,14 7,280 1,294" fill="var(--copper)"/>
    </svg>

    <p class="brand-name"><span>Pellor</span><span>Valley</span><span>Hospital</span></p>
  </section>
</body>
</html>
```